Plakat für Hersteller von maßgefertigten Tischunikaten aus Massivholz
Zielgruppe
Wir sind einen Firma die sich auf die Fertigung von maßgefertigten Tischunikaten aus Massivholz spezialisiert hat. Unsere Zielgruppe sind Design affine Leute, im Alter von 35-55 Jahren
Aufgabenstellung
Wir benötigen das Design für eine Messewand mit den Maßen 443X227 cm. 5 Zentimeter rundlaufen dürfen keine Elemente mehr platziert werden. Die Messewand steht im Hintergrund von unserem Stand bei verschiedenen Designmessen
Infos die auf die Messewand müssen: Logo, Tischmanufaktur aus Stuttgart, Maßgefertigte Tischunikate (Bei der Formulierung bin ich flexibel, ihr könnt bspw. auch nur Stichworte benutzen, aber Stuttgart und maßgefertigt ist wichtig).
Die Messewand soll sehr minimalistisch gestaltet sein, bei der letzten Messewand hatten wir ein Foto von einem Tisch im Hintergrund und das sah merkwürdig aus.

```html
<!DOCTYPE html>
<html lang="de">
<head>
<meta charset="utf-8">
<title>HOLLENBERG Manufaktur – Messewand</title>
<link rel="stylesheet" href="https://fonts.googleapis.com/css2?family=Inter:wght@200;300;500;600&display=swap">
<style>
  :root {
    --paper: #ffffff;
    --ink: #1b1b1b;
    --title: #333333;
    --muted: #a3a3a3;
    --divider: #d4d4d4;
    --night: #000000;
    --wood-light: #b89c74;
    --wood-mid: #7a6246;
    --cellar-light: #8a7352;
    --cellar-dark: #2e2619;
    --on-dark: #ffffff;
  }
  * { margin: 0; padding: 0; box-sizing: border-box; }
  html, body {
    width: 1200px; height: 615px; overflow: hidden;
    background: var(--paper);
    font-family: "Inter", "Helvetica Neue", Arial, sans-serif;
  }
  .wall { position: relative; width: 1200px; height: 615px; background: var(--paper); }

  .brand-mark {
    position: absolute; left: 42px; top: 41px;
    display: flex; align-items: center; gap: 12px;
  }
  .brand-mark__square { width: 40px; height: 40px; background: var(--night); }
  .brand-mark__name {
    font-weight: 500; font-size: 15px; letter-spacing: 3px; color: var(--ink);
  }

  .headline {
    position: absolute; left: 458px; top: 172px;
    white-space: nowrap; color: var(--title); font-weight: 200;
  }
  .headline__name { font-size: 61px; letter-spacing: 1px; }
  .headline__suffix { font-size: 42px; letter-spacing: 9px; margin-left: 12px; }

  .tagline {
    position: absolute; left: 458px; top: 250px;
    font-size: 19px; font-weight: 600; letter-spacing: 2.2px; color: var(--muted);
  }

  .band { position: absolute; left: 0; top: 314px; width: 1200px; height: 262px; }
  .band__hero {
    position: absolute; left: 0; top: 0; width: 876px; height: 262px;
    background:
      linear-gradient(90deg, var(--night) 0%, var(--night) 24%, rgba(0,0,0,0.6) 40%, rgba(0,0,0,0) 70%),
      linear-gradient(165deg, var(--night) 0%, var(--night) 26%, var(--wood-mid) 48%, var(--wood-light) 100%);
  }
  .band__divider {
    position: absolute; left: 876px; top: 0; width: 14px; height: 262px; background: var(--divider);
  }
  .band__detail {
    position: absolute; left: 890px; top: 1px; width: 269px; height: 260px;
    background: radial-gradient(ellipse at 40% 30%, var(--cellar-light) 0%, #5e4d35 50%, var(--cellar-dark) 100%);
  }
  .band__claim {
    position: absolute; left: 42px; top: 131px;
    color: var(--on-dark); font-size: 19px; font-weight: 500;
    letter-spacing: 4.2px; line-height: 23px;
  }
</style>
</head>
<body>
  <main class="wall">
    <div class="brand-mark">
      <span class="brand-mark__square"></span>
      <span class="brand-mark__name">HOLLENBERG</span>
    </div>

    <h1 class="headline">
      <span class="headline__name">HOLLENBERG</span><span class="headline__suffix">Manufaktur</span>
    </h1>
    <p class="tagline">Maßgefertigte Tischunikate</p>

    <section class="band">
      <div class="band__hero" role="img" aria-label="Massivholz-Tischplatte mit Maserung und Rissen im Dunkeln"></div>
      <div class="band__divider"></div>
      <div class="band__detail" role="img" aria-label="Massivholztisch mit schwarzen Stahlbeinen in einem Gewölbekeller"></div>
      <p class="band__claim">Tischmanufaktur<br>aus Stuttgart</p>
    </section>
  </main>
</body>
</html>
```